Fern Vale Ridgecrest Music Festival Poster

We are a summer music festival with concerts spanning Jazz, Cabaret, Education, Broadway, Chamber and Opera. We are looking for our key art for the 2016 season. This design will serve as the basis for all promotional materials, the concert program, and our web materials. Though eventually this means we will need to adjust the design to fit many different sizes, our poster will be printed mostly on 8.5" x 11" paper, and we can adapt from there. The design will be featured online and in print. It should be vertical and not landscape.

WE ARE SEEKING SLEEK, ELEGANT DESIGNS WITH MAYBE A KEY STOCK PHOTOGRAPH AND THE RELEVANT TEXT/DETAILS.

PLEASE NOTE: The included file "avenir logo.psd" is just a suggestion for the feel we are going for. It is our "working logo" after having scraped our old logo. We are interested in seeing your own ideas on how to style the brand name, but if you have ideas working with this version of the logo, feel free to use it.

REQUIRED DETAILS:
Festival Name: Fern Vale Ridgecrest Music Festival
Dates: July 29 - August 7 2016 (the year, 2016, must be included on the poster, but it does not need to be in the same location as where the actual dates are listed)
Website: www.fernvaleridgecrestfest.org

Additional Information:
- the 7 musical styles (jazz, choral, cabaret, education, broadway, chamber, opera) are important to defining who we are. You may decide to include these on the poster.
- We are looking for a very elegant design

TARGET:
We depend highly on an older clientele. We are working to expand our brand into younger demographics, but we want to be sure that we do not alienate our current consumer base with text that may be difficult for them to read.

Project Deadline Extended Reason: I am extending the deadline because it is taking longer to get feedback from my superiors than I had expected. Extending the deadline will give me time to provide adequate feedback from the people who will ultimately be making the decision. Thank you. Added Saturday, January 30, 2016

Sorry for the delay. There were issues with the decision makers but we are selecting in the next 24 hours.

Target Market(s)

Lovers of the styles of music we feature. We have a good number of elderly consumers, but also families and school groups (discussed further in description section)

Industry/Entity Type

Entertainment

Font styles to use
Sans Serif

Requirements
Must have
• Festival Name: Fern Vale Ridgecrest Music Festival
• Dates: July 29 - August 7 2016 (the year, 2016, must be included on the poster, but it does not need to be in the same location as where the actual dates are listed)
• Website: www.fernvaleridgecrestfest.org
Nice to have
• - the 7 musical styles (jazz, choral, cabaret, education, broadway, chamber, opera) are important to defining who we are. We would love to include these styles somewhere on the image, or feature them somehow in the artwork
• - Our brand has an elegance to it due to the type of music we offer, and our location being in a very natural space. inclusion of the music/nature mixed aspect of our brand in artwork might be nice
Should not have
• Anything that may offend or alienate an older, more conservative demographic

```html
<!DOCTYPE html>
<html lang="en">
<head>
<meta charset="utf-8">
<title>Fern Vale Ridgecrest Music Festival 2016</title>
<link rel="stylesheet" href="https://fonts.googleapis.com/css2?family=Montserrat:wght@400;700&family=Petit+Formal+Script&family=Playfair+Display:wght@900&display=swap">
<style>
  :root {
    --ink: #000000;
    --paper: #ffffff;
    --gold-light: #f6e6c4;
    --gold-mid: #f2c558;
    --gold-deep: #e6a530;
    --amber: #d9822f;
    --festival-yellow: #fde36a;
    --scroll-tone: #3a2808;
  }
  html, body {
    margin: 0;
    padding: 0;
    width: 1200px;
    height: 1200px;
    overflow: hidden;
    background: var(--paper);
  }
  .canvas {
    position: relative;
    width: 1200px;
    height: 1200px;
  }
  .poster {
    position: absolute;
    left: 256px;
    top: 148px;
    width: 708px;
    height: 900px;
    display: block;
  }
  .tagline, .style-list text {
    font-family: "Petit Formal Script", cursive;
    fill: var(--ink);
  }
  .festival-name {
    font-family: "Montserrat", sans-serif;
    font-weight: 400;
    fill: var(--paper);
  }
  .festival-kind {
    font-family: "Montserrat", sans-serif;
    font-weight: 700;
    fill: var(--festival-yellow);
  }
  .dates, .year {
    font-family: "Playfair Display", serif;
    font-weight: 900;
    font-variant-numeric: lining-nums;
  }
  .dates { fill: var(--paper); }
  .year { fill: var(--festival-yellow); }
  .website {
    font-family: "Montserrat", sans-serif;
    font-weight: 700;
    fill: var(--ink);
    letter-spacing: 2px;
  }
</style>
</head>
<body>
<main class="canvas">
  <svg class="poster" viewBox="0 0 885 1125" xmlns="http://www.w3.org/2000/svg">
    <defs>
      <linearGradient id="glow" x1="0" y1="0" x2="1" y2="1">
        <stop offset="0" stop-color="var(--gold-light)"/>
        <stop offset="0.45" stop-color="var(--gold-mid)"/>
        <stop offset="1" stop-color="var(--gold-deep)"/>
      </linearGradient>
      <linearGradient id="footer-glow" x1="0" y1="0" x2="1" y2="1">
        <stop offset="0" stop-color="var(--gold-mid)"/>
        <stop offset="0.7" stop-color="var(--gold-deep)"/>
        <stop offset="1" stop-color="var(--amber)"/>
      </linearGradient>
    </defs>

    <rect class="frame" x="0" y="0" width="885" height="1125" fill="var(--ink)"/>
    <rect class="backdrop" x="12" y="12" width="861" height="1101" fill="url(#glow)"/>

    <text class="tagline" x="442" y="108" font-size="60" text-anchor="middle">7 musical styles</text>

    <path class="title-band" d="M12,155 L672,155 C640,200 615,260 618,333 L12,333 Z" fill="var(--ink)"/>
    <text class="festival-name" x="80" y="235" font-size="50">Fern Vale Ridgecrest</text>
    <text class="festival-kind" x="80" y="302" font-size="56">MUSIC FESTIVAL</text>

    <g role="img" aria-label="Illustration of a carved string instrument scroll and tuning pegs">
      <rect x="692" y="158" width="146" height="640" rx="73" fill="var(--scroll-tone)"/>
    </g>

    <path class="hill" d="M12,820 C60,782 110,762 180,765 C280,770 350,822 480,836 C620,850 770,800 873,578 L873,1003 L12,1003 Z" fill="var(--ink)"/>

    <g role="img" aria-label="Silhouette of a music stand on the hilltop">
      <rect x="95" y="590" width="85" height="175" fill="var(--ink)"/>
    </g>

    <g class="style-list" text-anchor="end" font-size="50">
      <text x="610" y="395">jazz</text>
      <text x="610" y="460">choral</text>
      <text x="615" y="525">cabaret</text>
      <text x="625" y="592">education</text>
      <text x="655" y="662">broadway</text>
      <text x="652" y="732">chamber</text>
      <text x="645" y="795">opera</text>
    </g>

    <text class="dates" x="442" y="910" font-size="62" text-anchor="middle">July 29 - August 7</text>
    <text class="year" x="442" y="970" font-size="46" text-anchor="middle">2016</text>

    <rect class="footer-band" x="12" y="1003" width="861" height="110" fill="url(#footer-glow)"/>
    <text class="website" x="442" y="1068" font-size="36" text-anchor="middle">www.fernvaleridgecrestfest.org</text>
  </svg>
</main>
</body>
</html>
```